Webdesign für Personalvermittlung
Zielgruppe
Personalvermittlung
Aufgabenstellung
es soll einladend - nicht zu überladen und natürlich cool und modern sein

```html
<!DOCTYPE html>
<html lang="de">
<head>
<meta charset="utf-8">
<title>Pflegeweg – Personalvermittlung</title>
<link href="https://fonts.googleapis.com/css2?family=Manrope:wght@300;400;500;600;700;800&display=swap" rel="stylesheet">
<style>
:root{
  --green:#6abd45;
  --green-dark:#3f8a2e;
  --blue:#29a8e0;
  --ink:#3a3a3a;
  --text:#444;
  --white:#fff;
  --footer-bg:#f6f6f8;
  --line:#777;
}
*{box-sizing:border-box;margin:0;padding:0}
html,body{width:1200px;height:2593px;overflow:hidden;background:var(--white)}
body{font-family:'Manrope',sans-serif;color:var(--text);position:relative}
.abs{position:absolute}
.bg-shapes{position:absolute;left:0;top:0;width:1200px;height:2593px}
.brand{display:flex;align-items:center;gap:8px;font-weight:800;font-size:14px;color:var(--ink);letter-spacing:.5px}
.brand-dot{width:14px;height:14px;border-radius:50%;background:var(--green)}
.nav{display:flex;gap:40px;font-size:16px;font-weight:600}
.nav a{text-decoration:none;color:var(--white)}
.nav a.active{color:var(--green-dark)}
.hero-title{left:123px;top:152px;font-size:46px;font-weight:700;line-height:52px;color:var(--ink);letter-spacing:-.5px}
.hero-title .accent{color:var(--green)}
.hero-sub{left:123px;top:333px;font-size:21px;line-height:29px;color:var(--ink)}
.btn{display:inline-flex;align-items:center;gap:8px;background:var(--blue);color:var(--white);font-size:16px;border-radius:16px;height:32px;padding:0 22px;box-shadow:0 2px 6px rgba(0,0,0,.15)}
.link{color:var(--green);font-size:16px;display:flex;align-items:center;gap:8px}
.media{border-radius:8px}
.kicker{font-size:22px;color:var(--green);font-weight:400}
.section-title{font-size:37px;font-weight:700;color:var(--ink);line-height:42px;letter-spacing:-.3px}
.card{position:absolute;background:var(--white);border-radius:6px;box-shadow:0 2px 8px rgba(0,0,0,.12);padding:12px 13px}
.card-head{display:flex;gap:16px;align-items:flex-start;min-height:70px}
.card-head svg{flex:none}
.card-title{font-size:22px;font-weight:600;color:var(--ink);line-height:28px;margin-top:4px}
.card-text{font-size:16px;line-height:28px;color:var(--text);font-weight:400}
.testi-intro{left:123px;top:1540px;width:305px;font-size:16px;line-height:28px}
.quote-card{left:450px;top:1517px;width:627px;height:197px}
.quote-name{font-size:22px;font-weight:600;color:var(--ink);line-height:24px}
.quote-role{font-size:15px;color:var(--text)}
.field{position:absolute;background:var(--white);border-radius:16px;height:30px;padding:0 14px;font-size:16px;color:#aaa;display:flex;align-items:center;justify-content:space-between}
.field.filled{color:var(--ink)}
.footer{left:0;top:2468px;width:1200px;height:125px;background:var(--footer-bg)}
.foot-nav{display:flex;gap:42px;font-size:16px;color:var(--ink)}
.social{width:16px;height:16px;border-radius:50%;background:var(--line)}
.small{font-size:14px;color:var(--text)}
</style>
</head>
<body>

<svg class="bg-shapes" viewBox="0 0 1200 2593" aria-hidden="true">
  <polygon fill="var(--green)" points="560,0 1200,0 1200,475 1077,475 1077,122 622,122"/>
  <polygon fill="var(--green)" points="0,778 592,778 850,1272 0,1272"/>
  <polygon fill="var(--green)" points="587,1948 1200,1948 1200,2355 378,2355 330,2270 587,2270"/>
</svg>

<header>
  <div class="abs brand" style="left:125px;top:36px"><span class="brand-dot"></span>PFLEGEWEG</div>
  <nav class="abs nav" style="left:713px;top:39px">
    <a class="active">Home</a><a>Bewerber über uns</a><a>Wir über uns</a>
  </nav>
</header>

<section class="hero">
  <h1 class="abs hero-title">DEIN NÄCHSTER<br><span class="accent">KARRIERESCHRITT</span><br>IM PFLEGEBERUF!</h1>
  <p class="abs hero-sub">Wir bieten Dir den perfekten<br>Job als Führungskraft!</p>
  <span class="abs btn" style="left:123px;top:435px">Angebot bekommen</span>
  <span class="abs link" style="left:351px;top:442px">Wir bieten dir
    <svg width="18" height="10" viewBox="0 0 18 10"><path d="M0 5h16M12 1l4 4-4 4" stroke="currentColor" fill="none" stroke-width="1.5"/></svg></span>
  <div class="abs media" role="img" aria-label="Video: Arzt im weißen Kittel mit Stethoskop" style="left:532px;top:122px;width:545px;height:395px;background:linear-gradient(135deg,#c9a58d 0%,#d8dde4 40%,#a9b8c8 70%,#6e88a8 100%)"></div>
</section>

<section class="service">
  <p class="abs kicker" style="left:125px;top:613px">UNSER SERVICE</p>
  <h2 class="abs section-title" style="left:123px;top:641px">WAS DARFST DU VON UNS ERWARTEN?</h2>

  <article class="card" style="left:123px;top:717px;width:300px;height:256px">
    <div class="card-head">
      <svg width="46" height="38" viewBox="0 0 46 38" fill="none" stroke="var(--green)" stroke-width="2"><circle cx="23" cy="11" r="6"/><path d="M12 36c0-7 5-12 11-12s11 5 11 12z"/><circle cx="8" cy="8" r="4"/><circle cx="38" cy="8" r="4"/><path d="M1 22c0-4 3-7 7-7M45 22c0-4-3-7-7-7"/></svg>
      <h3 class="card-title">Zugriff auf mehr<br>Stellen</h3>
    </div>
    <p class="card-text">In Zusammenarbeit mit Einrichtungen und Kliniken erhalten unsere Kandidaten einen zugesicherten Bonus in Höhe von 750 EUR für das Vertrauen bei Ihrem Jobwechsel in pflegeweg-job.de</p>
  </article>

  <article class="card" style="left:450px;top:717px;width:300px;height:256px">
    <div class="card-head">
      <svg width="50" height="36" viewBox="0 0 50 36" fill="none" stroke="var(--green)" stroke-width="2"><rect x="2" y="6" width="46" height="26" rx="2"/><circle cx="25" cy="19" r="7"/><path d="M2 14c5 0 8-3 8-8M48 14c-5 0-8-3-8-8M2 24c5 0 8 3 8 8M48 24c-5 0-8 3-8 8"/></svg>
      <h3 class="card-title">100 % kostenfrei</h3>
    </div>
    <p class="card-text">Unsere Dienstleistung ist für Dich als Bewerber 100% kostenfrei! Es gibt auch garantiert keine versteckten Kosten!</p>
  </article>

  <article class="card" style="left:777px;top:717px;width:300px;height:256px">
    <div class="card-head">
      <svg width="60" height="36" viewBox="0 0 60 36" fill="none" stroke="var(--green)" stroke-width="2"><path d="M2 6h8v22H2M58 6h-8v22h8"/><path d="M10 10l10-4 8 4 10-4 12 4M10 26l12 6 8-4 6 2 14-8"/><path d="M28 10l-8 8 6 4 8-6"/></svg>
      <h3 class="card-title">Alle Versprechen<br>im Arbeitsvertrag</h3>
    </div>
    <p class="card-text">Du stellst Bedingungen an deinen neuen Arbeitgeber? - dann sorgen wir gemeinsam dafür, dass Du diese auch im Arbeitsvertrag findest - zu Deiner Sicherheit. Nichts ist schlimmer, als leere Versprechungen!</p>
  </article>

  <article class="card" style="left:123px;top:999px;width:300px;height:311px">
    <div class="card-head">
      <svg width="46" height="38" viewBox="0 0 46 38" fill="none" stroke="var(--green)" stroke-width="2"><path d="M4 4h24v16H12l-6 5v-5H4z"/><path d="M30 14h12v16h-2v5l-6-5H18v-6"/><path d="M13 9c0-2 6-2 6 1 0 2-3 2-3 4M16 17v1"/><path d="M25 26l3 2 5-5"/></svg>
      <h3 class="card-title">Dauerhafte<br>Betreuung</h3>
    </div>
    <p class="card-text">Dein neuer Arbeitgeber hält nicht was er verspricht? Keine Sorge, wir werden für Dich sofort wieder aktiv und bieten Dir schnell neue Möglichkeiten an - ohne dass Du erneut Bewerbungen versenden musst! Ein Anruf oder eine Email genügt!</p>
  </article>

  <article class="card" style="left:450px;top:999px;width:300px;height:311px">
    <div class="card-head">
      <svg width="40" height="38" viewBox="0 0 40 38" fill="none" stroke="var(--green)" stroke-width="2"><circle cx="20" cy="19" r="17"/><path d="M20 9v13M20 27v2"/></svg>
      <h3 class="card-title" style="margin-left:10px">Anonymität</h3>
    </div>
    <p class="card-text">Wir erstellen ein Profil Deiner Kenntnisse und Fähigkeiten sowie Deiner Berufserfahrung. Weder Dein Name, noch Deine Vorarbeitgeber tauchen im ersten Schritt auf. Erst wenn eine Einrichtung oder Klinik daran Interesse zeigt, entscheiden wir gemeinsam, wie es weitergeht!</p>
  </article>

  <article class="card" style="left:777px;top:999px;width:300px;height:311px">
    <div class="card-head">
      <svg width="40" height="38" viewBox="0 0 40 38" fill="none" stroke="var(--green)" stroke-width="2"><path d="M6 12a16 16 0 1 1-2 9"/><path d="M2 6l4 7 7-3"/><path d="M20 10v10l6 4"/></svg>
      <h3 class="card-title">Keine Zeitarbeit</h3>
    </div>
    <p class="card-text">Wir vermitteln ausschließlich in Festanstellungen direkt bei Kliniken oder Einrichtungen. Wir können Dir jedoch wertvolle Tipps geben, sollte Zeitarbeit für Dich in Frage kommen&nbsp;… WIR KENNEN UNS AUS!</p>
  </article>
</section>

<section class="testimonials">
  <p class="abs kicker" style="left:125px;top:1412px">TESTIMONIALS</p>
  <h2 class="abs section-title" style="left:123px;top:1441px">WAS BEWERBER ÜBER UNS SAGEN</h2>
  <p class="abs testi-intro">Durch die Stimmen unserer zufriedenen Kunden erhalten Sie einen ehrlichen Eindruck davon, wie wir arbeiten und welchen Wert wir unseren Kunden bieten.</p>
  <span class="abs btn" style="left:123px;top:1683px">Mehr Erfahrungen
    <svg width="18" height="10" viewBox="0 0 18 10"><path d="M0 5h16M12 1l4 4-4 4" stroke="currentColor" fill="none" stroke-width="1.5"/></svg></span>
  <article class="card quote-card" style="padding:14px 13px">
    <div style="display:flex;gap:18px;align-items:flex-start">
      <svg width="44" height="32" viewBox="0 0 44 32" fill="var(--green-dark)"><path d="M0 16C0 6 5 1 14 0v5c-4 1-6 4-6 8h8v19H0zM24 16c0-10 5-15 14-16v5c-4 1-6 4-6 8h8v19H24z"/></svg>
      <div><div class="quote-name">Max Muster</div><div class="quote-role">Leitung Musterbereich</div></div>
    </div>
    <p class="card-text" style="margin-top:14px">Lorem ipsum dolor sit amet, consetetur sadipscing elitr, sed diam nonumy eirmod tempor invidunt ut labore et dolore magna aliquyam erat, sed diam voluptua. At vero eos et accusam et justo duo dolores et ea rebum. Stet clita kasd gubergren, no sea takimata sanctus est Lorem ipsum dolor sit amet.</p>
  </article>
</section>

<section class="contact">
  <div class="abs media" role="img" aria-label="Foto: Gruppe junger, jubelnder Menschen" style="left:123px;top:1818px;width:464px;height:464px;background:linear-gradient(180deg,#e4e6e8 0%,#bfc3c6 45%,#8c9197 75%,#c8ccd0 100%)"></div>
  <p class="abs kicker" style="left:615px;top:1818px">KONTAKT</p>
  <h2 class="abs section-title" style="left:614px;top:1848px">WIR FREUEN UNS AUF<br>DICH</h2>
  <div class="field" style="left:614px;top:1974px;width:218px">Vorname*</div>
  <div class="field" style="left:859px;top:1974px;width:218px">Nachname*</div>
  <div class="field" style="left:614px;top:2020px;width:463px">E-Mail*</div>
  <div class="field filled" style="left:614px;top:2071px;width:218px">Rückruf erwünscht?
    <svg width="20" height="12" viewBox="0 0 20 12"><path d="M1 1l9 9 9-9" stroke="var(--ink)" stroke-width="2" fill="none"/></svg></div>
  <div class="field filled" style="left:859px;top:2071px;width:218px">Lebenslauf hochladen
    <svg width="20" height="18" viewBox="0 0 20 18" fill="none" stroke="var(--ink)" stroke-width="1.5"><path d="M2 2h2M2 9h2M2 16h2M8 2h10M8 9h10M8 16h10"/></svg></div>
  <div class="field" style="left:614px;top:2122px;width:463px;height:168px;align-items:flex-start;padding-top:6px">Nachricht</div>
  <span class="abs btn" style="left:614px;top:2310px;padding:0 20px;gap:18px">Absenden
    <svg width="22" height="16" viewBox="0 0 22 16" fill="none" stroke="currentColor" stroke-width="1.6"><rect x="1" y="1" width="20" height="14" rx="2"/><path d="M1 2l10 7 10-7"/></svg></span>
</section>

<footer class="abs footer">
  <div class="abs brand" style="left:125px;top:46px"><span class="brand-dot"></span>PFLEGEWEG</div>
  <nav class="abs foot-nav" style="left:717px;top:14px"><span>Home</span><span>Bewerber über uns</span><span>Wir über uns</span></nav>
  <div class="abs" style="left:1018px;top:56px;display:flex;gap:22px"><span class="social"></span><span class="social"></span></div>
  <div class="abs" style="left:123px;top:88px;width:954px;height:1px;background:var(--line)"></div>
  <p class="abs small" style="left:123px;top:100px">© 2024 farbwandel-studio.com</p>
  <p class="abs small" style="left:895px;top:100px;display:flex;gap:30px"><span>Impressum</span><span>Datenschutz</span></p>
</footer>

</body>
</html>
```